Brevimor Inc. Website

We need a website design for a new company based in Montreal, Canada. Our company offers professional services in planning & scheduling for major construction projects in varying industries. The main colors to be used are black & red (same as in logo). The final design should convey professionalism, precision, and excellence. The following are examples of what the website layout could look like: https://www.valqorix.ca/, https://4796.ca/, https://dumelvo.ca/, https://www.quorbintal.com/en. Avoid using stock videos or photos with people in it.
Target Market(s)
Target audience are multi-national clients looking to hire a firm to manage their construction projects. Target market is Mining & Metals
Industry/Entity Type
Mining & Metalurgy, Hydroelectricity, Infrastructure
Number of Pages Required
1 page
Colors
Designer to choose colors to be used in the design.
Look and feel
Each slider illustrates characteristics of the customer's brand and the style your logo design should communicate.

```html
<!DOCTYPE html>
<html lang="en">
<head>
<meta charset="utf-8">
<title>Brevimor Inc.</title>
<link href="https://fonts.googleapis.com/css2?family=Barlow:wght@400;500;600&display=swap" rel="stylesheet">
<style>
:root{
  --red:#a10a1c;
  --dark:#2b2b2d;
  --ink:#1e1e1e;
  --muted:#555;
  --grey:#f4f4f4;
  --footer:#1c1f24;
  --bar:#555759;
  --white:#fff;
}
*{box-sizing:border-box;margin:0;padding:0}
html,body{width:1200px;height:4380px;overflow:hidden}
body{font-family:"Barlow",sans-serif;color:var(--ink);background:var(--white)}
.page{position:relative;width:1200px;height:4380px;overflow:hidden}
.abs{position:absolute}
.photo{position:absolute}
.btn{position:absolute;display:flex;align-items:center;justify-content:center;border-radius:20px;font-size:10px;font-weight:500}
.btn-outline-light{border:1px solid rgba(255,255,255,.8);color:var(--white)}
.btn-red{background:var(--red);color:var(--white)}
.btn-outline-red{border:1px solid var(--red);color:var(--red)}
.btn-white{background:var(--white);color:var(--ink)}
.label{position:absolute;left:0;display:flex;align-items:center;font-size:10px;color:var(--red)}
.label::before{content:"";width:125px;height:1px;background:var(--red);margin-right:12px}
.label.light{color:var(--white)}
.label.light::before{background:var(--white)}
.h-sub{font-size:22px;line-height:30px;font-weight:400}
.small{font-size:10px;line-height:22px;color:var(--muted)}

/* header & hero */
.hero{position:absolute;left:0;top:0;width:1200px;height:531px;background:linear-gradient(120deg,#3d4148 0%,#5d6066 45%,#2e3035 100%)}
.hero-shade{position:absolute;inset:0;background:linear-gradient(90deg,rgba(20,20,22,.75),rgba(20,20,22,.25))}
.header-line{position:absolute;left:0;top:92px;width:1200px;height:1px;background:rgba(255,255,255,.35)}
.brand{position:absolute;left:75px;top:24px;display:flex;align-items:center;gap:8px;color:var(--white);font-size:20px;font-weight:600;letter-spacing:1px}
.brand-dot{width:14px;height:14px;border-radius:50%;background:var(--red)}
.nav{position:absolute;top:40px;font-size:10px;color:var(--white);font-weight:500}
.hero-title{position:absolute;left:137px;top:222px;width:500px;color:var(--white);font-size:30px;line-height:38px;font-weight:400}
.scroll-line{position:absolute;left:600px;top:445px;width:1px;height:65px;background:var(--white)}
.arrow-box{position:absolute;top:494px;width:37px;height:37px;background:var(--white);display:flex;align-items:center;justify-content:center;font-size:12px}

/* services */
.services{position:absolute;left:0;top:1058px;width:1200px;height:780px;background:var(--dark)}
.svc-item{position:absolute;left:343px;font-size:21px;color:#d8d8d8}

/* industries */
.ind-cap{position:absolute;top:2228px;width:182px;text-align:center;font-size:12px;color:var(--red)}

/* form */
.form{position:absolute;left:650px;top:3695px;width:412px;height:335px;background:var(--red);z-index:3}
.field{position:absolute;left:25px;width:362px;color:var(--white);font-size:9px;font-weight:600}
.field-line{position:absolute;left:25px;width:362px;height:1px;background:rgba(255,255,255,.45)}

/* footer */
.footer{position:absolute;left:0;top:3970px;width:1200px;height:365px;background:var(--footer)}
.f-h{position:absolute;top:4093px;font-size:13px;color:var(--white);font-weight:500}
.f-link{position:absolute;font-size:9px;color:#d0d0d0}
.social{position:absolute;top:4130px;width:20px;height:20px;border-radius:50%;background:#4a4d52}
</style>
</head>
<body>
<div class="page">

  <!-- Hero -->
  <section class="hero">
    <div class="photo" role="img" aria-label="Construction professionals in hard hats reviewing plans on site" style="inset:0;background:linear-gradient(120deg,#50545b,#8a8c90 55%,#3a3c41)"></div>
    <div class="hero-shade"></div>
  </section>
  <div class="brand"><span class="brand-dot"></span>BREVIMOR</div>
  <div class="nav" style="left:405px">Home</div>
  <div class="nav" style="left:468px">About Us</div>
  <div class="nav" style="left:545px">Services</div>
  <div class="nav" style="left:621px">Projects</div>
  <div class="nav" style="left:692px">News/Blog</div>
  <div class="nav" style="left:778px">Contact Us</div>
  <div class="nav" style="left:870px;display:flex;align-items:center;gap:5px">
    <svg width="9" height="9" viewBox="0 0 24 24"><path fill="#fff" d="M6.6 10.8a15 15 0 0 0 6.6 6.6l2.2-2.2c.3-.3.7-.4 1-.2 1.1.4 2.3.6 3.6.6.6 0 1 .4 1 1V20c0 .6-.4 1-1 1C10.6 21 3 13.4 3 4c0-.6.4-1 1-1h3.5c.6 0 1 .4 1 1 0 1.3.2 2.5.6 3.6.1.3 0 .7-.2 1z"/></svg>555-014-2210</div>
  <div class="btn btn-outline-light" style="left:1000px;top:28px;width:125px;height:36px">Consult Now</div>
  <div class="header-line"></div>
  <h1 class="hero-title">We offers Professional Services in Planning &amp; Scheduling for Major Construction Projects</h1>
  <div class="btn btn-outline-light" style="left:137px;top:362px;width:125px;height:36px">Contact Us</div>
  <div class="scroll-line"></div>
  <div class="arrow-box" style="left:985px">&#8249;</div>
  <div class="arrow-box" style="left:1025px">&#8250;</div>

  <!-- About -->
  <div class="label" style="top:604px">About Us</div>
  <h2 class="abs" style="left:612px;top:603px;width:390px;font-size:22px;line-height:30px;font-weight:400">Lorem Ipsum is simply dummy text of the printing and typesetting industry. Lorem Ipsum has been the industry's standard dummy text ever since the 1500s,</h2>
  <p class="abs small" style="left:612px;top:793px;width:400px">There are many variations of passages of Lorem Ipsum available, but the majority have suffered alteration in some form, by injected humour, or randomised words which don't look even slightly believable. If you are going to use a passage of lorem ipsum</p>
  <div class="btn btn-red" style="left:612px;top:930px;width:113px;height:35px">Discover More</div>

  <!-- Services -->
  <section class="services" role="img" aria-label="Dark background of planning documents and charts on a desk" style="background:linear-gradient(90deg,#2a2a2c,#333336 50%,#252527)"></section>
  <div class="abs" style="left:1125px;top:1030px;width:75px;height:30px;background:var(--dark)"></div>
  <div class="photo" role="img" aria-label="Team working together at a laptop in an office" style="left:137px;top:680px;width:413px;height:442px;background:linear-gradient(135deg,#d7d9dc,#9ea3aa 55%,#6f7278);z-index:2"></div>
  <div class="label light" style="top:1209px">Our Services</div>
  <h2 class="abs h-sub" style="left:318px;top:1186px;width:480px;color:var(--white)">Lorem Ipsum is simply dummy text of the printing and typesetting industry</h2>
  <svg class="abs" style="left:200px;top:1365px" width="70" height="65" viewBox="0 0 70 65" fill="none" stroke="#cfcfcf" stroke-width="2">
    <rect x="4" y="6" width="46" height="36"/><line x1="27" y1="42" x2="27" y2="56"/><line x1="18" y1="58" x2="36" y2="58"/>
    <rect x="12" y="26" width="5" height="10" fill="#a10a1c" stroke="none"/><rect x="21" y="20" width="5" height="16" fill="#a10a1c" stroke="none"/><rect x="30" y="14" width="5" height="22" fill="#a10a1c" stroke="none"/>
    <circle cx="54" cy="46" r="9" stroke="#a10a1c"/><circle cx="54" cy="46" r="3" stroke="#a10a1c"/>
  </svg>
  <div class="abs" style="left:318px;top:1335px;width:1px;height:205px;background:#6a6a6a"></div>
  <div class="svc-item" style="top:1347px">Project Management</div>
  <div class="svc-item" style="top:1391px;color:var(--red)">Project Controls</div>
  <div class="svc-item" style="top:1435px">Procurement and Contract Management</div>
  <div class="svc-item" style="top:1479px">Construction</div>
  <div class="svc-item" style="top:1523px">PMO-Project Management office</div>
  <p class="abs" style="left:343px;top:1586px;width:370px;font-size:10px;line-height:22px;color:var(--white)">Lorem Ipsum is simply dummy text of the printing typesetting industry. Lorem Ipsum has been the industry's standard dummy text ever since the 1500s, when an unknown printer took a galley of type and scrambled it to make.</p>
  <div class="btn btn-outline-light" style="left:343px;top:1703px;width:125px;height:37px">Explore More</div>
  <div class="photo" role="img" aria-label="Hands with pencils reviewing bar and pie charts on a tablet" style="left:793px;top:1307px;width:407px;height:438px;background:linear-gradient(135deg,#e8ecf2,#b9c4d6 55%,#8e9cb8)"></div>
  <div class="abs" style="left:137px;top:1808px;width:988px;height:30px;background:var(--white)"></div>

  <!-- Industries -->
  <div class="label" style="top:1922px">Industries</div>
  <h2 class="abs h-sub" style="left:300px;top:1900px;width:600px;text-align:center">Lorem Ipsum is simply dummy text of the printing and typesetting industry</h2>
  <div class="photo" role="img" aria-label="Open-pit mine seen from above" style="left:200px;top:1990px;width:182px;height:220px;background:linear-gradient(180deg,#8aa0b5,#8c8a86 40%,#6b6965)"></div>
  <div class="photo" role="img" aria-label="Worker handling hot metal in a foundry" style="left:406px;top:1990px;width:182px;height:220px;background:linear-gradient(160deg,#3b4c5c,#8a6a4c 55%,#2d3a44)"></div>
  <div class="photo" role="img" aria-label="Hydroelectric dam by a lake and hills" style="left:612px;top:1990px;width:182px;height:220px;background:linear-gradient(180deg,#7fa4c6,#5d7a63 45%,#9aa19a)"></div>
  <div class="photo" role="img" aria-label="Cable-stayed bridge over water" style="left:818px;top:1990px;width:182px;height:220px;background:linear-gradient(180deg,#b8ccdf,#d6dde4 60%,#8a98a6)"></div>
  <div class="ind-cap" style="left:200px">Mining &amp;amp</div>
  <div class="ind-cap" style="left:406px">Metallurgy</div>
  <div class="ind-cap" style="left:612px">Hydroelectricity</div>
  <div class="ind-cap" style="left:818px">Infrastructure</div>
  <div class="btn btn-red" style="left:537px;top:2280px;width:125px;height:35px">Consult Now</div>

  <!-- Grey band -->
  <div class="abs" style="left:0;top:2520px;width:893px;height:1110px;background:var(--grey)"></div>

  <!-- Grow -->
  <section class="abs" style="left:75px;top:2378px;width:925px;height:294px;background:var(--red);color:var(--white)">
    <h2 class="abs" style="left:62px;top:70px;font-size:29px;font-weight:500">Let's Grow Together</h2>
    <p class="abs" style="left:62px;top:122px;width:340px;font-size:16px;line-height:21px">Have questions about your next growth move? Brevimor has answers.</p>
    <div class="btn btn-white" style="left:62px;top:195px;width:125px;height:35px">Consult Now</div>
    <div class="abs" style="left:560px;top:95px;display:flex;align-items:center;gap:14px;font-size:34px;font-weight:600;letter-spacing:3px">
      <span style="width:40px;height:40px;border-radius:50%;background:var(--white)"></span>BREVIMOR</div>
  </section>

  <!-- News -->
  <div class="label" style="top:2734px">News</div>
  <h2 class="abs" style="left:137px;top:2860px;font-size:22px;font-weight:500">Recent Articles</h2>
  <p class="abs" style="left:137px;top:2900px;width:245px;font-size:12px;line-height:19px;color:var(--muted)">There are many variations of passages of lorem ipsum available, but the majority have suffered alteration in some form injected humour.</p>
  <div class="photo" role="img" aria-label="House model, drafting tools and hard hat on blueprints" style="left:406px;top:2780px;width:387px;height:280px;background:linear-gradient(160deg,#cfd6c8,#d9cdb8 55%,#a88a66)"></div>
  <div class="abs" style="left:406px;top:3085px;font-size:14px;font-weight:500">Contrary to popular belief</div>
  <p class="abs small" style="left:406px;top:3114px;width:300px;line-height:15px">There are many variations of passages of lorem ipsum available, but the majority.</p>
  <div class="photo" role="img" aria-label="View of a bridge through a concrete arch" style="left:818px;top:2810px;width:244px;height:218px;background:linear-gradient(180deg,#3c4046,#8ea7bf 45%,#77797c)"></div>
  <div class="abs" style="left:818px;top:3052px;width:220px;font-size:14px;line-height:17px;font-weight:500">There are many variations of passages of lorem Ipsum available</div>
  <div class="photo" role="img" aria-label="Glass skyscrapers seen from below against blue sky" style="left:137px;top:3225px;width:451px;height:180px;background:linear-gradient(180deg,#3f6d9c,#9dbbd8 55%,#c9d4de)"></div>
  <div class="abs" style="left:137px;top:3432px;font-size:14px;font-weight:500">Contrary to Popular Belief</div>
  <p class="abs small" style="left:137px;top:3460px;width:300px;line-height:15px">There are many variations of passages of lorem ipsum available, but the majority.</p>
  <div class="photo" role="img" aria-label="Desk with calculator, glasses and financial charts" style="left:612px;top:3200px;width:281px;height:280px;background:linear-gradient(135deg,#e9e4c6,#dfe4ea 55%,#a9b8cb)"></div>
  <div class="abs" style="left:918px;top:3295px;width:150px;font-size:14px;line-height:17px;font-weight:500">It is a long established fact that a reader</div>
  <p class="abs small" style="left:918px;top:3357px;width:140px;line-height:14px">There are many variations of passages of lorem</p>
  <div class="btn btn-outline-red" style="left:537px;top:3532px;width:125px;height:36px">View All News</div>

  <!-- Consult -->
  <div class="label" style="top:3746px">Consult Now</div>
  <h2 class="abs h-sub" style="left:137px;top:3795px;width:420px">If You Find a Hight Quality <span style="color:var(--red)">Consultant</span> for Your Projects?</h2>
  <div class="abs" style="left:137px;top:3872px;font-size:18px;color:var(--red)">Talk to Our Talented Team Member</div>

  <!-- Footer -->
  <footer class="footer" role="img" aria-label="Dark aerial view of a city highway at night" style="background:linear-gradient(180deg,#22262c,#15181c)"></footer>
  <div class="form">
    <div class="field" style="top:45px">Name</div><div class="field-line" style="top:67px"></div>
    <div class="field" style="top:83px">Phone</div><div class="field-line" style="top:105px"></div>
    <div class="field" style="top:121px">Email</div><div class="field-line" style="top:143px"></div>
    <div class="field" style="top:158px">Message</div><div class="field-line" style="top:212px"></div>
    <div class="btn btn-outline-light" style="left:157px;top:238px;width:100px;height:37px">Send</div>
  </div>
  <div class="abs" style="left:137px;top:4115px;display:flex;align-items:center;gap:10px;color:var(--white);font-size:24px;font-weight:600;letter-spacing:2px"><span style="width:22px;height:22px;border-radius:50%;background:var(--red)"></span>BREVIMOR</div>
  <div class="f-h" style="left:398px">Contact Us</div>
  <svg class="abs" style="left:398px;top:4135px" width="11" height="11" viewBox="0 0 24 24"><path fill="#a10a1c" d="M6.6 10.8a15 15 0 0 0 6.6 6.6l2.2-2.2c.3-.3.7-.4 1-.2 1.1.4 2.3.6 3.6.6.6 0 1 .4 1 1V20c0 .6-.4 1-1 1C10.6 21 3 13.4 3 4c0-.6.4-1 1-1h3.5c.6 0 1 .4 1 1 0 1.3.2 2.5.6 3.6.1.3 0 .7-.2 1z"/></svg>
  <div class="abs" style="left:423px;top:4132px;font-size:13px;color:var(--white)">555-014-2210</div>
  <svg class="abs" style="left:398px;top:4167px" width="11" height="9" viewBox="0 0 22 16"><rect x="1" y="1" width="20" height="14" fill="none" stroke="#a10a1c" stroke-width="2"/><path d="M1 1l10 8 10-8" fill="none" stroke="#a10a1c" stroke-width="2"/></svg>
  <div class="f-link" style="left:423px;top:4166px">support@brevimor.ca</div>
  <svg class="abs" style="left:398px;top:4195px" width="10" height="13" viewBox="0 0 20 26"><path d="M10 1a8 8 0 0 0-8 8c0 6 8 16 8 16s8-10 8-16a8 8 0 0 0-8-8z" fill="#a10a1c"/><circle cx="10" cy="9" r="3" fill="#1c1f24"/></svg>
  <div class="f-link" style="left:423px;top:4194px;width:160px;line-height:14px">88 Harbour Row, Montreal QC H2X 1Y4</div>
  <div class="f-h" style="left:642px">Quick Links</div>
  <div class="f-link" style="left:642px;top:4134px">Home</div>
  <div class="f-link" style="left:642px;top:4156px">About Us</div>
  <div class="f-link" style="left:642px;top:4178px">Services</div>
  <div class="f-link" style="left:642px;top:4200px">Projects</div>
  <div class="f-link" style="left:642px;top:4222px">News/Blog</div>
  <div class="f-link" style="left:642px;top:4244px">Contact Us</div>
  <div class="f-link" style="left:715px;top:4134px">Term &amp; Conditions</div>
  <div class="f-link" style="left:715px;top:4156px">Privacy Policy</div>
  <div class="f-h" style="left:855px">Follow Us</div>
  <div class="social" style="left:856px"></div>
  <div class="social" style="left:886px;background:var(--red)"></div>
  <div class="social" style="left:916px"></div>
  <div class="social" style="left:946px"></div>
  <svg class="abs" style="left:1124px;top:4112px" width="14" height="14" viewBox="0 0 14 14"><path d="M7 1L13 13L7 10L1 13Z" fill="#c8102e"/></svg>
  <div class="abs" style="left:75px;top:4335px;width:1125px;height:45px;background:var(--bar);display:flex;align-items:center;justify-content:center;font-size:9px;color:var(--white)">&copy; 2023 Brevimor. All Rights Reserved</div>

</div>
</body>
</html>
```